Larkspur Homes - wanted BRILLIANT website design for our new property investing company

We need a website design for our new company based in Bristol, England, UK called "Larkspur Homes". We help buy people property who are in financial difficulty or who are needing to sell their property quickly for reasons such as death, divorce/separation, relocation, emigration.

We have a logo being designed incorporating strawberry and property (so red and green). We would like designs to communicate an elegant ,professional, approachable, friendly
fresh clean but also warm appealing appearance
Not too busy
Website consistent with logo and company name i.e. colour scheme

Please use our word document for content as a guide but use professional judgement for minor alterations if you feel they would benefit the site/structure etc

Please ask at any time if not sure

Target Market(s)

Adult british population, those that have a mortgage / loan / own property

Industry/Entity Type

Financial

Font styles to use
Serif
Sans Serif
Decorative

Colors
0692cd
33b7a4
acd036
fbee3e
3176b5
886aae
a6479a
e567a6
eb1f27

Requirements
Must have
• This must not look like a template website we are looking for UNIQUE please!
Nice to have
• Bristol pictures instead of generic, or colourful line drawings/comic drawings of houses/property/keys/happy people.....
Should not have
• An obvious off the shelf template design

```html
<!DOCTYPE html>
<html lang="en">
<head>
<meta charset="utf-8">
<title>Larkspur Homes</title>
<link href="https://fonts.googleapis.com/css2?family=Montserrat:wght@400;600;700&family=Open+Sans:wght@400;600;700&family=Lato:wght@400;700&display=swap" rel="stylesheet">
<style>
:root{
  --green:#4aab26;
  --red:#d0103a;
  --ink:#333;
  --muted:#666;
  --line:#e3e3e3;
  --footer:#454545;
  --footer-bottom:#222;
  --white:#fff;
}
*{box-sizing:border-box;margin:0;padding:0}
html,body{width:1200px;height:2683px;overflow:hidden}
body{position:relative;background:var(--white);font-family:"Open Sans",Arial,sans-serif;color:var(--ink)}
.abs{position:absolute}

/* header */
.site-header{position:absolute;left:0;top:0;width:1200px;height:129px;background:var(--white)}
.brand{position:absolute;left:122px;top:48px;display:flex;align-items:center;gap:10px;font-family:"Montserrat",sans-serif;font-weight:600;font-size:22px;color:var(--red)}
.brand-dot{width:14px;height:14px;border-radius:50%;background:var(--red)}
.contact-line{position:absolute;right:122px;top:22px;display:flex;gap:30px;font-size:15px;color:var(--ink);align-items:center}
.contact-line span{display:flex;align-items:center;gap:9px}
.main-nav{position:absolute;right:122px;top:70px;display:flex;gap:27px;font-size:14.5px;color:#555}
.main-nav .active{color:var(--green)}

/* hero */
.hero{position:absolute;left:0;top:129px;width:1200px;height:590px;background:linear-gradient(160deg,#a98471 0%,#c59d85 30%,#8a6c5e 60%,#6d5650 100%)}
.hero-shade{position:absolute;inset:0;background:rgba(40,30,25,.25)}
.hero-title{position:absolute;top:48px;left:0;width:100%;text-align:center;font-family:"Montserrat",sans-serif;font-weight:700;font-size:38px;line-height:54px;color:var(--white);text-transform:uppercase;letter-spacing:.5px;text-shadow:0 2px 6px rgba(0,0,0,.35)}
.reasons{position:absolute;top:207px;left:180px;display:flex;gap:40px;color:var(--white);font-family:"Montserrat",sans-serif;font-size:21px}
.reason{display:flex;align-items:center;gap:16px}
.reason-icon{width:40px;height:40px;background:var(--green);display:flex;align-items:center;justify-content:center}
.search-box{position:absolute;left:130px;top:373px;width:939px;height:104px;background:var(--white);box-shadow:0 3px 10px rgba(0,0,0,.3);display:flex;gap:15px;padding:28px}
.field{width:219px;height:46px;border:1px solid #d8d8d8;border-radius:2px;font-size:13px;color:#999;padding:0 15px;display:flex;align-items:center;justify-content:space-between}
.search-btn{width:186px;height:46px;background:var(--red);color:var(--white);font-weight:600;font-size:18px;display:flex;align-items:center;justify-content:center;border-radius:2px}

/* welcome */
.welcome{position:absolute;left:129px;top:758px;width:540px}
h2.section-title{font-family:"Montserrat",sans-serif;font-weight:400;font-size:24px;color:var(--ink)}
.welcome p{margin-top:22px;font-size:12.2px;line-height:24px;color:var(--muted)}
.btn-green{display:inline-flex;align-items:center;justify-content:center;background:var(--green);color:var(--white);font-size:14px;font-weight:600;width:118px;height:38px;margin-top:26px}
.specialties{position:absolute;left:751px;top:758px;width:320px}
.specialties ul{margin-top:20px;list-style:none}
.specialties li{font-size:13.6px;color:#555;line-height:27px;padding-left:22px;position:relative}
.specialties li::before{content:"";position:absolute;left:4px;top:12px;width:5px;height:5px;border-radius:50%;background:#555}
.divider{position:absolute;left:130px;top:1091px;width:935px;height:2px;background:var(--line)}

/* properties */
.props-head{position:absolute;left:128px;top:1137px;width:938px;height:46px;border-bottom:1px solid var(--line);display:flex;align-items:center}
.props-head h3{font-family:"Montserrat",sans-serif;font-weight:400;font-size:22px;text-transform:uppercase;color:var(--ink)}
.tabs{margin-left:48px;display:flex}
.tab{font-size:11.5px;padding:6px 10px;border:1px solid #ccc;color:#999}
.tab.on{background:var(--green);border-color:var(--green);color:var(--white)}
.arrows{margin-left:auto;display:flex}
.arrow{width:31px;height:31px;border:1px solid #ccc;background:var(--white);display:flex;align-items:center;justify-content:center;font-size:15px;color:#999}
.prop-card{position:absolute;top:1201px;width:215px;height:292px;border:1px solid #e2e2e2;box-shadow:0 1px 3px rgba(0,0,0,.1);background:var(--white)}
.prop-photo{height:161px}
.prop-body{padding:14px 13px}
.prop-name{font-size:12.5px;color:var(--green);font-weight:600;white-space:nowrap}
.prop-loc{font-size:11px;color:#555;margin-top:2px}
.prop-meta{display:flex;gap:16px;margin-top:13px;font-size:11px;color:#666}
.prop-meta span{display:flex;align-items:center;gap:5px}
.prop-foot{position:absolute;bottom:0;left:0;right:0;height:41px;border-top:1px solid #e4e4e4;background:#f6f6f6;display:flex}
.price{flex:1;display:flex;align-items:center;padding-left:14px;color:var(--green);font-size:14px}
.details{width:84px;border-left:1px solid #e0e0e0;display:flex;align-items:center;justify-content:center;font-size:12px;color:#555}

/* testimonials */
.testimonials{position:absolute;left:0;top:1556px;width:1200px;height:398px;background:linear-gradient(180deg,#e9e9e7,#d9d9d6 60%,#cfcfcb)}
.testimonials .veil{position:absolute;inset:0;background:rgba(255,255,255,.55)}
.testimonials h2{position:absolute;left:132px;top:42px;font-family:"Montserrat",sans-serif;font-weight:400;font-size:28px;color:var(--ink)}
.testimonials .arrows{position:absolute;left:1005px;top:38px}
.quote-card{position:absolute;top:143px;width:460px;height:170px;background:var(--white);box-shadow:0 2px 6px rgba(0,0,0,.2)}
.avatar{position:absolute;left:25px;top:28px;width:108px;height:108px;border-radius:50%;border:4px solid var(--white);box-shadow:0 0 0 1px #ccc;background:linear-gradient(135deg,#c7b7a8,#8f7c70)}
.quote{position:absolute;left:146px;top:26px;width:300px;padding-left:14px}
.quote-text{font-size:12.2px;line-height:20px;color:#777}
.mark{font-family:Georgia,serif;font-size:22px;color:#666;font-weight:700;line-height:0}
.mark.open{position:absolute;left:-4px;top:4px}
.mark.close{display:inline-block;margin-left:96px;position:relative;top:14px}
.quote .name{color:var(--red);font-size:13px;font-weight:600;margin-top:16px}
.quote .role{font-size:11.5px;color:#666;margin-top:2px}

/* blog */
.blog-title{position:absolute;left:132px;top:2007px;font-family:"Montserrat",sans-serif;font-weight:400;font-size:28px}
.post{position:absolute;top:2080px;width:470px;height:153px}
.post-photo{position:absolute;left:0;top:0;width:231px;height:153px}
.post-date{position:absolute;left:10px;top:12px;background:var(--red);color:var(--white);font-size:12px;padding:6px 10px;display:flex;gap:12px}
.post-date span{display:flex;align-items:center;gap:5px}
.post-text{position:absolute;left:248px;top:0;width:222px}
.post-text h4{font-family:"Lato",sans-serif;font-weight:700;font-size:16px;color:#222;white-space:nowrap}
.tags{font-size:12px;color:var(--red);margin-top:6px;display:flex;align-items:center;gap:6px}
.post-text p{font-size:11.8px;line-height:22px;color:#555;margin-top:8px;width:216px}
.more{font-size:12.3px;color:var(--red);margin-top:10px}

/* footer */
.site-footer{position:absolute;left:0;top:2307px;width:1200px;height:314px;background:var(--footer);color:var(--white)}
.site-footer h5{font-family:"Open Sans",sans-serif;font-weight:700;font-size:15px}
.fcol{position:absolute;top:42px}
.fcol ul{list-style:none;margin-top:18px}
.fcol li{font-size:12.3px;line-height:25px;color:#eee}
.input{width:213px;height:26px;background:var(--white);margin-top:8px;font-size:10.5px;font-style:italic;color:#666;padding:5px 8px}
.input.first{margin-top:14px}
.input.area{height:56px}
.submit{width:88px;height:28px;background:var(--green);font-weight:700;font-size:14px;display:flex;align-items:center;justify-content:center;margin-top:14px}
.recent p{margin-top:18px;font-size:12.3px;line-height:25px;color:#eee;width:255px}
.copyright{position:absolute;left:0;top:2621px;width:1200px;height:62px;background:var(--footer-bottom);color:var(--white);font-size:12px;display:flex;align-items:center;justify-content:center}
</style>
</head>
<body>

<svg width="0" height="0" style="position:absolute">
  <defs>
    <symbol id="icon-car" viewBox="0 0 20 11"><path d="M2 6l2-4h10l3 4h2v3H1V6z" fill="#4aab26"/><path d="M5 3h4v3H4zM10 3h3l2 3h-5z" fill="#fff"/><circle cx="5" cy="9" r="2" fill="#4aab26" stroke="#fff"/><circle cx="15" cy="9" r="2" fill="#4aab26" stroke="#fff"/></symbol>
    <symbol id="icon-bed" viewBox="0 0 20 11"><rect x="0" y="1" width="2" height="10" fill="#4aab26"/><rect x="3" y="3" width="4" height="3" rx="1" fill="#4aab26"/><rect x="2" y="6" width="18" height="3" fill="#4aab26"/><rect x="18" y="6" width="2" height="5" fill="#4aab26"/></symbol>
    <symbol id="icon-bath" viewBox="0 0 20 11"><path d="M1 4h18v2c0 2-2 4-4 4H5C3 10 1 8 1 6z" fill="#4aab26"/><path d="M3 4V1h3" fill="none" stroke="#4aab26" stroke-width="1.5"/></symbol>
  </defs>
</svg>

<header class="site-header">
  <div class="brand"><span class="brand-dot"></span>Larkspur Homes</div>
  <div class="contact-line">
    <span><svg width="18" height="14" viewBox="0 0 18 14"><rect x="1" y="1" width="16" height="12" fill="none" stroke="#555" stroke-width="1.5"/><path d="M1 1l8 7 8-7" fill="none" stroke="#555" stroke-width="1.5"/></svg>info@larkspur-homes.co.uk</span>
    <span><svg width="12" height="18" viewBox="0 0 12 18"><rect x="1" y="1" width="10" height="16" rx="2" fill="none" stroke="#555" stroke-width="1.5"/><rect x="5" y="13" width="2" height="2" fill="#555"/></svg>0700-3158206</span>
  </div>
  <nav class="main-nav">
    <span class="active">Home</span><span>Sell your property fast</span><span>Rent Your property fast</span><span>The 5 easy step</span><span>About</span><span>Contact</span>
  </nav>
</header>

<section class="hero">
  <div class="abs" style="inset:0" role="img" aria-label="Photo of cupped hands holding a house key"></div>
  <div class="hero-shade"></div>
  <h1 class="hero-title">Does the government have unclaimed<br>your property?</h1>
  <div class="reasons">
    <div class="reason"><span class="reason-icon"><svg width="20" height="22" viewBox="0 0 20 22"><path d="M8 2h4v5h6v4h-6v9H8v-9H2V7h6z" fill="#fff"/></svg></span>Death</div>
    <div class="reason"><span class="reason-icon"><svg width="22" height="22" viewBox="0 0 22 22"><path d="M11 2L2 10h3v10h12V10h3z" fill="#fff"/><rect x="9" y="13" width="4" height="7" fill="#4aab26"/></svg></span>Divorce/Seperation</div>
    <div class="reason"><span class="reason-icon"><svg width="20" height="20" viewBox="0 0 20 20"><path d="M5 10a6 6 0 1 0 2-4.5" fill="none" stroke="#fff" stroke-width="3"/><path d="M3 2v7h7z" fill="#fff"/></svg></span>Relocation</div>
    <div class="reason"><span class="reason-icon"><svg width="22" height="22" viewBox="0 0 22 22"><path d="M2 12l18-9-6 17-3-6z" fill="#fff"/></svg></span>Emigration</div>
  </div>
  <div class="search-box">
    <div class="field">First Name</div>
    <div class="field">Last Name</div>
    <div class="field">State<svg width="8" height="6" viewBox="0 0 8 6"><path d="M0 0h8L4 6z" fill="#444"/></svg></div>
    <div class="search-btn">Search</div>
  </div>
</section>

<section class="welcome">
  <h2 class="section-title">Welcome to Larkspur Homes</h2>
  <p>Lorem ipsum dolor sit amet, consectetur adipisicing elit, sed do eiusmod tempor incididunt ut labore et dolore magna aliqua. sed do eiusmod tempor consectetur adipisicing elit, sed do eiusmod tempor incididunt ut labore et dolore magna aliqua.Lorem ipsum dolor sit amet, consectetur adipisicing elit, sed do eiusmod tempor incididunt ut labore et dolore magna aliqua. sed do eiusmod tempor consectetur adipisicing elit, sed do eiusmod tempor incididunt ut labore et dolore magna aliqua incididunt ut labore et dolore magna aliqua eiusmod tempor incididunt ut labore et dolore magna aliqua incididunt.</p>
  <span class="btn-green">Read More</span>
</section>

<section class="specialties">
  <h2 class="section-title">We Specialize In:</h2>
  <ul>
    <li>Buying Properties Quickly</li>
    <li>Finding Creative solutions to your property</li>
    <li>Propert rental management</li>
    <li>Lettings to professional and student tenants</li>
    <li>Guaranteed rent and management schemes</li>
    <li>Stopping repossessions</li>
    <li>Motivated Sellers</li>
    <li>Chain Fixing</li>
    <li>Negative Equity Problems</li>
  </ul>
</section>

<div class="divider"></div>

<div class="props-head">
  <h3>Hot Properties</h3>
  <div class="tabs"><span class="tab on">For Rent</span><span class="tab">For Sale</span></div>
  <div class="arrows"><span class="arrow">&lsaquo;</span><span class="arrow">&rsaquo;</span></div>
</div>

<article class="prop-card" style="left:129px">
  <div class="prop-photo" role="img" aria-label="Photo of a white villa with a pool" style="background:linear-gradient(180deg,#7fb2e0,#e8e4da 55%,#4fa7c9)"></div>
  <div class="prop-body"><div class="prop-name">6 Bedrooms Villa in Clifton</div><div class="prop-loc">Clifton, Bristol</div>
  <div class="prop-meta"><span>3 <svg width="20" height="11"><use href="#icon-car"/></svg></span><span>6 <svg width="20" height="11"><use href="#icon-bed"/></svg></span><span>8 <svg width="20" height="11"><use href="#icon-bath"/></svg></span></div></div>
  <div class="prop-foot"><span class="price">£ 25,000</span><span class="details">Details</span></div>
</article>
<article class="prop-card" style="left:370px">
  <div class="prop-photo" role="img" aria-label="Photo of city apartment towers" style="background:linear-gradient(180deg,#a9c6e2,#8a9fb3 50%,#5e6f7e)"></div>
  <div class="prop-body"><div class="prop-name">2 Bedrooms Apartment</div><div class="prop-loc">Harbourside Residence, Bristol</div>
  <div class="prop-meta"><span>3 <svg width="20" height="11"><use href="#icon-car"/></svg></span><span>6 <svg width="20" height="11"><use href="#icon-bed"/></svg></span><span>8 <svg width="20" height="11"><use href="#icon-bath"/></svg></span></div></div>
  <div class="prop-foot"><span class="price">£ 66,000</span><span class="details">Details</span></div>
</article>
<article class="prop-card" style="left:610px">
  <div class="prop-photo" role="img" aria-label="Photo of a city skyline at dusk" style="background:linear-gradient(180deg,#1f3b66,#3d5a86 50%,#c99a52 80%,#6a4b2c)"></div>
  <div class="prop-body"><div class="prop-name">2 Bedrooms Villa in Redland</div><div class="prop-loc">Redland, Bristol</div>
  <div class="prop-meta"><span>3 <svg width="20" height="11"><use href="#icon-car"/></svg></span><span>6 <svg width="20" height="11"><use href="#icon-bed"/></svg></span><span>8 <svg width="20" height="11"><use href="#icon-bath"/></svg></span></div></div>
  <div class="prop-foot"><span class="price">£ 125,000</span><span class="details">Details</span></div>
</article>
<article class="prop-card" style="left:851px">
  <div class="prop-photo" role="img" aria-label="Photo of a family walking by apartment buildings" style="background:linear-gradient(180deg,#c9b9a0,#b59b7a 60%,#8b7a66)"></div>
  <div class="prop-body"><div class="prop-name">4 Bedrooms Villa in Clifton</div><div class="prop-loc">Clifton, Bristol</div>
  <div class="prop-meta"><span>3 <svg width="20" height="11"><use href="#icon-car"/></svg></span><span>6 <svg width="20" height="11"><use href="#icon-bed"/></svg></span><span>8 <svg width="20" height="11"><use href="#icon-bath"/></svg></span></div></div>
  <div class="prop-foot"><span class="price">£ 155,000</span><span class="details">Details</span></div>
</article>

<section class="testimonials">
  <div class="abs" style="inset:0" role="img" aria-label="Faded photo of a bright living room interior"></div>
  <div class="veil"></div>
  <h2>Testimonials</h2>
  <div class="arrows"><span class="arrow">&lsaquo;</span><span class="arrow">&rsaquo;</span></div>
  <div class="quote-card" style="left:129px">
    <div class="avatar" role="img" aria-label="Portrait photo of the client"></div>
    <div class="quote"><span class="mark open">&ldquo;</span>
      <div class="quote-text">Its is a long established fact that a reader will be distracted by the readable content of a page when looking at its layout<span class="mark close">&rdquo;</span></div>
      <div class="name">Daniel Hartley</div><div class="role">CEO, Company Name</div></div>
  </div>
  <div class="quote-card" style="left:606px">
    <div class="avatar" role="img" aria-label="Portrait photo of the client"></div>
    <div class="quote"><span class="mark open">&ldquo;</span>
      <div class="quote-text">Its is a long established fact that a reader will be distracted by the readable content of a page when looking at its layout<span class="mark close">&rdquo;</span></div>
      <div class="name">Oliver Prentice</div><div class="role">CEO, Company Name</div></div>
  </div>
</section>

<h2 class="blog-title">From the Blog</h2>
<article class="post" style="left:129px">
  <div class="post-photo" role="img" aria-label="Photo of a modern red and white living room" style="background:linear-gradient(135deg,#d9d5d0,#b8b2ab 50%,#c0392b 75%,#eee)"></div>
  <div class="post-date"><span><svg width="11" height="11" viewBox="0 0 11 11"><rect x="0.5" y="1.5" width="10" height="9" fill="none" stroke="#fff"/><rect x="0.5" y="1.5" width="10" height="3" fill="#fff"/></svg>April 06 2013</span><span><svg width="12" height="11" viewBox="0 0 12 11"><path d="M1 1h10v6H5l-3 3V7H1z" fill="#fff"/></svg>16</span></div>
  <div class="post-text"><h4>Nullam dignisim vivera sceler</h4><div class="tags"><svg width="10" height="10"><path d="M0 0h5l5 5-5 5-5-5z" fill="#999"/></svg>teger, luctus, porttitor, purus</div>
  <p>Lorem ipsum dolor sit amet, consectetur adipiscing elit. Praesent pulvinar massa nec augue malesuada in</p><div class="more">Read More &raquo;</div></div>
</article>
<article class="post" style="left:609px">
  <div class="post-photo" role="img" aria-label="Photo of a modern kitchen with dining table" style="background:linear-gradient(135deg,#3a3a3a,#8a8a8a 45%,#e8e6e2 70%,#b22)"></div>
  <div class="post-date"><span><svg width="11" height="11" viewBox="0 0 11 11"><rect x="0.5" y="1.5" width="10" height="9" fill="none" stroke="#fff"/><rect x="0.5" y="1.5" width="10" height="3" fill="#fff"/></svg>April 06 2013</span><span><svg width="12" height="11" viewBox="0 0 12 11"><path d="M1 1h10v6H5l-3 3V7H1z" fill="#fff"/></svg>16</span></div>
  <div class="post-text"><h4>Nullam dignisim vivera sceler</h4><div class="tags"><svg width="10" height="10"><path d="M0 0h5l5 5-5 5-5-5z" fill="#999"/></svg>teger, luctus, porttitor, purus</div>
  <p>Lorem ipsum dolor sit amet, consectetur adipiscing elit. Praesent pulvinar massa nec augue malesuada in</p><div class="more">Read More &raquo;</div></div>
</article>

<footer class="site-footer">
  <div class="fcol" style="left:134px">
    <h5>Contact Us</h5>
    <div class="input first">Enter your name..</div>
    <div class="input">Enter your email</div>
    <div class="input">Property Address</div>
    <div class="input area">Enter your message</div>
    <div class="submit">Submit</div>
  </div>
  <div class="fcol" style="left:417px">
    <h5>Sitemap</h5>
    <ul><li>Home</li><li>About Us</li><li>Rent</li><li>Sell</li><li>Special Offers</li><li>Easy 5 Steps</li><li>Contact Us</li></ul>
  </div>
  <div class="fcol" style="left:606px">
    <h5>Products</h5>
    <ul><li>Lorem Ipsum Dolor</li><li>Sit amet and Industry</li><li>That is all set</li><li>With this Type</li><li>And So On</li><li>With Lorem</li><li>And Ending</li></ul>
  </div>
  <div class="fcol recent" style="left:828px">
    <h5>Recent Posts</h5>
    <p>Lorem Ipsum is simply dummy text of the printing and typesetting industry. Lorem Ipsum has been the industry's standard dummy text ever since the 1500s, when an unknown printer took a galley of type and scrambled it to make a type specimen book.</p>
  </div>
</footer>
<div class="copyright">Copyright &copy; 2013 Larkspur Homes. All Rights Reserved</div>

</body>
</html>
```